Business card and stationary for Auto Parts
Vern's Auto Parts
Use same font as used in my logo
Dale Korthauer
Manager
2457 E. 14 Birch Lane
vernsautoparts@kelvomail.com
www.vernsautoparts-demo.com
Store Hours:
Monday-Friday 8am-6pm
Saturday 8am-3pm
add small qv logo

```html
<!DOCTYPE html>
<html lang="en">
<head>
<meta charset="utf-8">
<title>Vern's Auto Parts – Business Cards</title>
<link rel="stylesheet" href="https://fonts.googleapis.com/css2?family=Arimo:wght@400;700&display=swap">
<style>
  :root {
    --stage: #d9d6d1;
    --paper: #ffffff;
    --ink: #3a3a3a;
    --black: #0b0b0b;
    --red: #b0121b;
    --red-deep: #5a070c;
    --white: #ffffff;
    --chrome: #c9cdd2;
  }
  * { margin: 0; padding: 0; box-sizing: border-box; }
  html, body { width: 1200px; height: 737px; overflow: hidden; }
  body {
    background: var(--stage);
    font-family: "Arimo", Arial, sans-serif;
    position: relative;
  }
  .card {
    position: absolute;
    width: 540px;
    height: 283px;
    overflow: hidden;
    box-shadow: 0 4px 12px rgba(0,0,0,.35);
  }
  .card--front-light { left: 36px;  top: 53px;  background: var(--paper); }
  .card--back-light  { left: 629px; top: 53px;  background: var(--paper); }
  .card--front-dark  { left: 36px;  top: 384px; background: var(--black); }
  .card--back-dark   { left: 629px; top: 384px; background: var(--black); }

  .band {
    position: absolute; left: 0; top: 0; width: 100%; height: 128px;
    background: linear-gradient(90deg, #050505 0%, #1a0304 30%, var(--red-deep) 45%, var(--red) 62%, var(--red-deep) 80%, #090909 100%);
  }
  .band::after {
    content: ""; position: absolute; inset: 0;
    background: linear-gradient(180deg, rgba(255,255,255,.12) 0%, rgba(0,0,0,0) 40%, rgba(0,0,0,.35) 100%);
  }

  .brand {
    position: absolute;
    display: flex; align-items: center; gap: 10px;
  }
  .brand__dot {
    width: 22px; height: 22px; border-radius: 50%;
    background: var(--red); border: 3px solid var(--chrome);
    flex: none;
  }
  .brand__name {
    font-weight: 700; font-size: 30px; letter-spacing: .5px;
    color: var(--red); white-space: nowrap;
  }
  .card--front-light .brand, .card--front-dark .brand { left: 28px; top: 62px; }
  .card--front-light .brand__name, .card--front-dark .brand__name { font-size: 24px; color: var(--white); }
  .card--back-dark .brand__name { color: var(--white); }
  .card--back-light .brand, .card--back-dark .brand { left: 110px; top: 100px; }

  .holder { position: absolute; left: 307px; top: 26px; color: var(--white); }
  .holder__name { font-weight: 700; font-size: 17px; }
  .holder__title { font-size: 13px; margin-top: 4px; opacity: .9; }

  .contact {
    position: absolute; left: 307px; top: 158px;
    font-size: 11.5px; line-height: 15px; color: var(--ink);
  }
  .contact__address { margin-bottom: 14px; }
  .contact__web { margin-top: 14px; }
  .card--front-dark .contact { color: var(--white); }

  .hours {
    position: absolute; right: 22px; bottom: 18px;
    display: flex; align-items: flex-start; gap: 10px;
    color: var(--ink); font-size: 13px; line-height: 15px;
  }
  .hours__social {
    display: flex; align-items: center; gap: 5px; margin-top: 1px;
    font-weight: 700; font-size: 13px;
  }
  .hours__social-mark {
    width: 12px; height: 12px; background: var(--red); flex: none;
  }
  .hours__title, .hours__days { font-weight: 700; }
  .hours__time { font-weight: 400; }
  .card--back-dark .hours { color: var(--white); }
</style>
</head>
<body>

<section class="card card--front-light" aria-label="Business card front, light">
  <div class="band"></div>
  <div class="brand"><span class="brand__dot"></span><span class="brand__name">Vern's Auto Parts</span></div>
  <div class="holder">
    <p class="holder__name">Dale Korthauer</p>
    <p class="holder__title">Manager</p>
  </div>
  <div class="contact">
    <p class="contact__address">2457 E. 14 Birch Lane</p>
    <p>P: (555)014-2206</p>
    <p>F: (555)014-2366</p>
    <p>E: vernsautoparts@kelvomail.com</p>
    <p class="contact__web">www.vernsautoparts-demo.com</p>
  </div>
</section>

<section class="card card--back-light" aria-label="Business card back, light">
  <div class="brand"><span class="brand__dot"></span><span class="brand__name">Vern's Auto Parts</span></div>
  <div class="hours">
    <span class="hours__social"><span class="hours__social-mark"></span>qv</span>
    <div>
      <p class="hours__title">Store Hours:</p>
      <p><span class="hours__days">Monday-Friday</span> <span class="hours__time">8am-6pm</span></p>
      <p><span class="hours__days">Saturday</span> <span class="hours__time">8am-3pm</span></p>
    </div>
  </div>
</section>

<section class="card card--front-dark" aria-label="Business card front, dark">
  <div class="band"></div>
  <div class="brand"><span class="brand__dot"></span><span class="brand__name">Vern's Auto Parts</span></div>
  <div class="holder">
    <p class="holder__name">Dale Korthauer</p>
    <p class="holder__title">Manager</p>
  </div>
  <div class="contact">
    <p class="contact__address">2457 E. 14 Birch Lane</p>
    <p>P: (555)014-2206</p>
    <p>F: (555)014-2366</p>
    <p>E: vernsautoparts@kelvomail.com</p>
    <p class="contact__web">www.vernsautoparts-demo.com</p>
  </div>
</section>

<section class="card card--back-dark" aria-label="Business card back, dark">
  <div class="brand"><span class="brand__dot"></span><span class="brand__name">Vern's Auto Parts</span></div>
  <div class="hours">
    <span class="hours__social"><span class="hours__social-mark"></span>qv</span>
    <div>
      <p class="hours__title">Store Hours:</p>
      <p><span class="hours__days">Monday-Friday</span> <span class="hours__time">8am-6pm</span></p>
      <p><span class="hours__days">Saturday</span> <span class="hours__time">8am-3pm</span></p>
    </div>
  </div>
</section>

</body>
</html>
```